Business Card for an IT professional services company
Lakeshore Datavault Inc.
Business Card for an IT professional services company - Information Technology
Creative Brief
Professional
Martin Keswell
President
2718 5th Avenue SE Calgary, Alberta T2H 4B7
mart@lakeshoredatavault.example
www.lakeshoredatavault.example

```html
<!DOCTYPE html>
<html lang="en">
<head>
<meta charset="utf-8">
<title>Lakeshore Datavault – Business Card</title>
<link rel="stylesheet" href="https://fonts.googleapis.com/css2?family=Open+Sans:wght@400;600;700&display=swap">
<style>
  :root {
    --bg: #d9d9d9;
    --card: #ffffff;
    --blue: #1c5a9c;
    --tab: #8a8a8d;
    --navy: #1f3f73;
    --red: #c4302b;
    --ink: #4a4a4a;
    --white: #ffffff;
  }
  * { margin: 0; padding: 0; box-sizing: border-box; }
  html, body { width: 1200px; height: 895px; overflow: hidden; }
  body {
    background: var(--bg);
    font-family: "Open Sans", Arial, sans-serif;
    position: relative;
  }
  .card {
    position: absolute;
    left: 100px; top: 162px;
    width: 1000px; height: 571px;
    background: var(--card);
    box-shadow: 0 10px 30px rgba(0,0,0,.18);
    overflow: hidden;
  }
  .corner-tab { position: absolute; right: 0; top: 0; width: 230px; height: 110px; }
  .brand {
    position: absolute; left: 60px; top: 70px;
    display: flex; align-items: center; gap: 14px;
  }
  .brand-mark { width: 22px; height: 22px; background: var(--navy); }
  .brand-name { font-size: 40px; font-weight: 600; color: var(--navy); letter-spacing: -0.5px; }
  .contact-panel {
    position: absolute; left: 30px; top: 250px;
    width: 620px; height: 290px;
    background: var(--blue);
    border-radius: 18px 0 0 18px;
    display: flex;
  }
  .contact-cell {
    flex: 1;
    display: flex; flex-direction: column; align-items: center; justify-content: center;
    gap: 26px; color: var(--white); font-size: 19px; text-align: center; padding: 0 16px;
  }
  .contact-cell + .contact-cell { border-left: 3px solid var(--white); }
  .contact-cell svg { width: 54px; height: 54px; }
  .contact-lines { line-height: 1.6; }
  .identity { position: absolute; left: 680px; top: 262px; width: 290px; }
  .person-name { font-size: 30px; color: var(--red); font-weight: 400; letter-spacing: 1px; }
  .person-name .surname { color: var(--ink); }
  .person-title { font-size: 15px; color: var(--ink); letter-spacing: 2px; margin-top: 4px; }
  .address-cell {
    position: absolute; left: 653px; top: 360px;
    width: 317px; height: 180px;
    background: var(--blue);
    border-radius: 0 18px 18px 0;
    border-left: 3px solid var(--white);
    color: var(--white);
    display: flex; flex-direction: column; align-items: center; justify-content: center;
    gap: 16px; font-size: 16px; text-align: center; padding: 0 20px; line-height: 1.5;
  }
  .address-cell svg { width: 40px; height: 40px; }
</style>
</head>
<body>
  <main class="card">
    <svg class="corner-tab" viewBox="0 0 230 110" aria-hidden="true">
      <polygon points="40,0 230,0 230,110 0,110 0,40 40,40" fill="var(--tab)"/>
    </svg>

    <div class="brand">
      <span class="brand-mark"></span>
      <span class="brand-name">Lakeshore Datavault</span>
    </div>

    <section class="contact-panel">
      <div class="contact-cell phone">
        <svg viewBox="0 0 24 24" aria-hidden="true"><path fill="#fff" d="M6.6 10.8a15.1 15.1 0 0 0 6.6 6.6l2.2-2.2c.3-.3.7-.4 1-.2 1.1.4 2.3.6 3.6.6.6 0 1 .4 1 1V20c0 .6-.4 1-1 1A17 17 0 0 1 3 4c0-.6.4-1 1-1h3.5c.6 0 1 .4 1 1 0 1.3.2 2.5.6 3.6.1.3 0 .7-.2 1z"/></svg>
        <div class="contact-lines">012 555 0147<br>012 555 0148</div>
      </div>
      <div class="contact-cell web">
        <svg viewBox="0 0 24 24" aria-hidden="true" fill="none" stroke="#fff" stroke-width="1.6"><circle cx="12" cy="12" r="9.5"/><ellipse cx="12" cy="12" rx="4" ry="9.5"/><path d="M2.5 12h19M4 7h16M4 17h16"/></svg>
        <div class="contact-lines">mart@lakeshoredatavault.example<br>www.lakeshoredatavault.example</div>
      </div>
    </section>

    <div class="identity">
      <div class="person-name">MARTIN <span class="surname">KESWELL</span></div>
      <div class="person-title">PRESIDENT</div>
    </div>

    <div class="address-cell">
      <svg viewBox="0 0 24 24" aria-hidden="true"><path fill="#fff" d="M12 2a7 7 0 0 0-7 7c0 5 7 13 7 13s7-8 7-13a7 7 0 0 0-7-7zm0 9.5A2.5 2.5 0 1 1 12 6.5a2.5 2.5 0 0 1 0 5z"/></svg>
      <div>2718 5th Avenue SE<br>Calgary, Alberta T2H 4B7</div>
    </div>
  </main>
</body>
</html>
```